Business Card Design

Semi retired Estate Agent opening new small business. I am not chasing or wanting to sell everyday houses.. I quite like land and development sales or special projects
..Will need letterheads design and electronic header for electronic mail.
Would like the wording of "Built On Years Of Trust".Envisage simple design..max 3 colours..have strong belief in red , white and blue colours on white background

Would think that the words "Neil Harcombe" be bigger than the words "Real Estate"
I don't want it too busy as many cards are..also has to be classy..!!!
Bold card with my name and mobile number and "Built On Years Of Trust" on the main side and the details on the reverse.
But I am open to suggestions.!!!!!

Target Market(s)

Possible other real estate agents in Western Australia..semi commercial clients.

Industry/Entity Type

Electronic

Contact Information for Business Card

Neil Harcombe Real Estate

Neil Harcombe
Principal and Licensee
neil@neilharcombere.com.au
mobile 0427581934
ph/f 08 96172385 4B Wattlebank Pde,Claremont ,WA,6010

Requirements
Must have
• I do like the term Built On Years Of Trust"..The reverse side to have address etc..the face side to have name and m obile number

```html
<!DOCTYPE html>
<html lang="en">
<head>
<meta charset="utf-8">
<title>Neil Harcombe Real Estate – Business Card</title>
<link rel="stylesheet" href="https://fonts.googleapis.com/css2?family=PT+Sans:ital,wght@0,400;0,700;1,700&display=swap">
<style>
  :root {
    --navy: #14325a;
    --red: #ff0000;
    --white: #ffffff;
  }
  html, body {
    margin: 0;
    padding: 0;
    width: 1110px;
    height: 1200px;
    overflow: hidden;
    background: var(--white);
  }
  .canvas {
    position: relative;
    width: 1110px;
    height: 1200px;
    background: var(--white);
    font-family: "PT Sans", Tahoma, sans-serif;
    color: var(--navy);
  }
  .corner-band {
    position: absolute;
    width: 320px;
    height: 232px;
  }
  .corner-band--front-top { left: 65px; top: 60px; }
  .corner-band--front-bottom { left: 723px; top: 360px; }
  .corner-band--back-top { left: 65px; top: 604px; }
  .corner-band--back-bottom { left: 723px; top: 905px; }

  .text {
    position: absolute;
    margin: 0;
    white-space: nowrap;
    line-height: 1;
  }
  .agency-name {
    display: flex;
    align-items: center;
    gap: 18px;
    font-weight: 700;
    font-size: 54px;
  }
  .agency-name .marker {
    width: 26px;
    height: 26px;
    background: var(--red);
    flex: none;
  }
  .front .agency-name { left: 200px; top: 300px; }
  .back .agency-name { left: 330px; top: 680px; }
  .tagline {
    left: 67px; top: 466px;
    font-weight: 700;
    font-style: italic;
    font-size: 52px;
    letter-spacing: 1px;
  }
  .front-mobile {
    left: 69px; top: 545px;
    font-size: 42px;
    letter-spacing: 0.5px;
  }
  .role {
    left: 95px; top: 823px;
    font-size: 42px;
  }
  .details {
    position: absolute;
    left: 95px; top: 913px;
    margin: 0;
    font-size: 38px;
    line-height: 45px;
    font-style: normal;
    letter-spacing: 0.5px;
  }
  .details span { display: block; white-space: nowrap; }
  .details .label { display: inline; margin-right: 20px; }
</style>
</head>
<body>
<div class="canvas">
  <svg width="0" height="0" style="position:absolute" aria-hidden="true">
    <defs>
      <g id="band">
        <polygon points="0,170 236,0 300,0 0,216" fill="var(--red)"/>
      </g>
    </defs>
  </svg>

  <section class="front">
    <svg class="corner-band corner-band--front-top" viewBox="0 0 320 232" aria-hidden="true"><use href="#band"/></svg>
    <svg class="corner-band corner-band--front-bottom" viewBox="0 0 320 232" aria-hidden="true"><use href="#band" transform="rotate(180 160 116)"/></svg>
    <h1 class="text agency-name"><span class="marker"></span>Neil Harcombe Real Estate</h1>
    <p class="text tagline">Built On Years Of Trust</p>
    <p class="text front-mobile">042 758 1934</p>
  </section>

  <section class="back">
    <svg class="corner-band corner-band--back-top" viewBox="0 0 320 232" aria-hidden="true"><use href="#band"/></svg>
    <svg class="corner-band corner-band--back-bottom" viewBox="0 0 320 232" aria-hidden="true"><use href="#band" transform="rotate(180 160 116)"/></svg>
    <h2 class="text agency-name"><span class="marker"></span>Neil Harcombe Real Estate</h2>
    <p class="text role">Principal and Licensee</p>
    <address class="details">
      <span><span class="label">Mobile</span>042 758 1934</span>
      <span><span class="label">Tel/Fax</span>(08) 9617 2385</span>
      <span>4B Wattlebank Pde</span>
      <span>Westhaven, WA, 6099</span>
      <span>neil@neilharcombere.com.au</span>
    </address>
  </section>
</div>
</body>
</html>
```